Stationary pack
Stationary
Project: Stationary pack
Stationary pack - Construction
Creative Brief
Simple
Derek Olsworth
318 Harrowdene Lane Stoketon Brackmere Wessex BK7 4RB
brightlinejoiner@mailvane.net

```html
<!DOCTYPE html>
<html lang="en">
<head>
<meta charset="utf-8">
<title>Derek Olsworth Kitchen Fitter – Business Cards</title>
<link href="https://fonts.googleapis.com/css2?family=Arimo:wght@400;700&display=swap" rel="stylesheet">
<style>
  :root {
    --bg: #3a3a3c;
    --card: #ffffff;
    --brand-blue: #1f78c8;
    --frame-grey: #a9abae;
    --wave-grey: #a7a9ac;
    --text-grey: #4a4a4a;
    --icon-grey: #5b5e63;
  }
  * { margin: 0; padding: 0; box-sizing: border-box; }
  html, body {
    width: 1200px; height: 940px; overflow: hidden;
    background: var(--bg);
    font-family: "Arimo", Arial, sans-serif;
  }
  .canvas { position: relative; width: 1200px; height: 940px; }

  .card {
    position: absolute;
    width: 620px; height: 354px;
    border-radius: 22px;
    overflow: hidden;
    background: var(--card);
  }

  /* Front */
  .card-front { left: 90px; top: 90px; background: var(--brand-blue); padding: 14px; }
  .card-front .inner {
    width: 100%; height: 100%;
    background: var(--card);
    border: 10px solid var(--frame-grey);
    border-radius: 12px;
    display: flex; align-items: center; justify-content: center;
  }

  .brand { display: flex; align-items: center; gap: 14px; color: var(--brand-blue); }
  .brand-square { width: 54px; height: 54px; background: var(--brand-blue); border-radius: 4px; flex: none; }
  .brand-name {
    font-weight: 400; text-transform: uppercase; line-height: 1.15;
    font-size: 30px; letter-spacing: 1px; color: var(--brand-blue);
  }
  .brand-name span { display: block; font-size: 20px; letter-spacing: 3.4px; }

  /* Back */
  .card-back { left: 490px; top: 496px; }
  .card-back .brand { position: absolute; top: 54px; right: 40px; gap: 10px; }
  .card-back .brand-square { width: 36px; height: 36px; }
  .card-back .brand-name { font-size: 20px; }
  .card-back .brand-name span { font-size: 13px; letter-spacing: 2.3px; }

  .holder-name {
    position: absolute; left: 40px; top: 118px;
    font-size: 26px; font-weight: 700; color: var(--brand-blue);
  }
  .contact {
    position: absolute; left: 40px; top: 180px;
    font-size: 12.5px; color: var(--text-grey); line-height: 1.5;
    list-style: none;
  }
  .contact li { display: flex; align-items: center; gap: 8px; }
  .contact .address { margin-bottom: 6px; display: block; }
  .contact svg { width: 12px; height: 12px; fill: var(--icon-grey); flex: none; }

  .wave { position: absolute; left: 0; bottom: 0; width: 620px; height: 354px; }
</style>
</head>
<body>
<main class="canvas">

  <section class="card card-front" aria-label="Business card front">
    <div class="inner">
      <div class="brand">
        <div class="brand-square"></div>
        <div class="brand-name">Derek Olsworth<span>Kitchen Fitter</span></div>
      </div>
    </div>
  </section>

  <section class="card card-back" aria-label="Business card back">
    <svg class="wave" viewBox="0 0 620 354" preserveAspectRatio="none" aria-hidden="true">
      <path d="M0,354 L0,282 C210,318 440,290 620,120 L620,354 Z" fill="var(--wave-grey)"/>
      <path d="M0,354 L0,300 C220,334 450,306 620,160 L620,354 Z" fill="#ffffff"/>
      <path d="M0,354 L0,310 C230,346 460,318 620,182 L620,354 Z" fill="var(--brand-blue)"/>
    </svg>

    <div class="brand">
      <div class="brand-square"></div>
      <div class="brand-name">Derek Olsworth<span>Kitchen Fitter</span></div>
    </div>

    <h1 class="holder-name">Derek Olsworth</h1>

    <ul class="contact">
      <li class="address">318 Harrowdene Lane<br>Stoketon, Brackmere, Wessex BK7 4RB</li>
      <li>
        <svg viewBox="0 0 12 12" aria-hidden="true"><path d="M3 0h6a1 1 0 0 1 1 1v10a1 1 0 0 1-1 1H3a1 1 0 0 1-1-1V1a1 1 0 0 1 1-1zm0 2v7h6V2z"/></svg>
        07700 900418
      </li>
      <li>
        <svg viewBox="0 0 12 12" aria-hidden="true"><path d="M0 2h12v8H0z"/><path d="M1 3l5 3.4L11 3" stroke="#fff" stroke-width="1" fill="none"/></svg>
        brightlinejoiner@mailvane.net
      </li>
    </ul>
  </section>

</main>
</body>
</html>
```